Carton Box Packaging For Motorcycle Brake Shoe - Varonel Brand

Packaging Dimensions: 125mm (H) x 125mm (W) x 31mm (D)
We would like to design a genuine Carton box Packaging for motorcycle Brake Shoe.
This is a critical part of the motorcycle, so we need the packaging to reflect elegant impression.
Varonel, is one of the leading companies for manufacturing Motorcycles, located in Egypt. Our company is offering high-quality products, the best in the local market, with very competitive prices.
We have a limited time to get this project done, So we Highly appreciate receiving your designs ASAP.
Target Market(s)
Economical Motorcycle Buyers
Colors
Designer to choose colors to be used in the design.
Look and feel

```html
<!DOCTYPE html>
<html lang="en">
<head>
<meta charset="utf-8">
<title>Varonel Brake Pads Carton</title>
<link rel="stylesheet" href="https://fonts.googleapis.com/css2?family=Exo+2:ital,wght@0,700;0,800;1,800;1,900&display=swap">
<style>
  :root {
    --page: #eef0f2;
    --royal-blue: #0a3fa6;
    --deep-blue: #08359a;
    --signal-yellow: #ffc906;
    --gold: #c9a20b;
    --race-red: #ff1a12;
    --label-white: #ffffff;
    --label-grey: #c9c9c9;
    --ink: #0b0b0b;
    --pale-text: #d9dce6;
    --rider-tan: #b89a3a;
  }
  * { margin: 0; padding: 0; box-sizing: border-box; }
  html, body { width: 1200px; height: 830px; overflow: hidden; background: var(--page); }
  body { position: relative; font-family: "Exo 2", sans-serif; }

  .carton { position: absolute; left: 320px; top: 45px; width: 560px; }

  .lid { position: relative; width: 560px; height: 560px; background: var(--royal-blue); overflow: hidden; }
  .lid-graphics { position: absolute; inset: 0; }

  .rider-artwork {
    position: absolute; left: 120px; top: 55px; width: 370px; height: 275px;
    background: radial-gradient(ellipse at 50% 55%, rgba(184,154,58,.55), rgba(184,154,58,.15) 70%, rgba(184,154,58,0));
    border-radius: 40px;
  }

  .brand-lockup { position: absolute; display: flex; align-items: center; gap: 8px; color: var(--label-white); font-weight: 800; letter-spacing: 1px; }
  .brand-dot { width: 34px; height: 34px; border-radius: 50%; background: var(--label-grey); }
  .lid .brand-lockup { right: 26px; top: 60px; font-size: 24px; }

  .lid-kicker {
    position: absolute; left: 200px; top: 285px; width: 290px; height: 44px;
    background: var(--royal-blue); color: var(--label-white);
    font-size: 34px; font-weight: 900; font-style: italic; line-height: 44px; text-align: center;
    transform: skewX(-12deg);
  }
  .lid-title {
    position: absolute; left: 30px; top: 332px; width: 510px; height: 78px;
    background: var(--label-white); box-shadow: -14px 10px 0 var(--race-red);
    color: var(--ink); font-size: 66px; font-weight: 900; font-style: italic;
    line-height: 78px; text-align: center; letter-spacing: 1px;
  }

  .front-panel { position: relative; width: 560px; height: 150px; background: var(--deep-blue); overflow: hidden; }
  .front-panel svg { position: absolute; inset: 0; }
  .front-kicker {
    position: absolute; left: 150px; top: 18px; width: 220px; text-align: center;
    color: var(--pale-text); font-size: 24px; font-weight: 800; font-style: italic;
  }
  .front-title {
    position: absolute; left: 130px; top: 52px; width: 250px; height: 50px;
    background: var(--label-grey); box-shadow: -10px 8px 0 var(--race-red);
    color: var(--ink); font-size: 36px; font-weight: 800; font-style: italic;
    line-height: 50px; text-align: center;
  }
  .front-panel .brand-lockup { right: 16px; top: 58px; font-size: 17px; flex-direction: column; gap: 4px; }
  .front-panel .brand-dot { width: 44px; height: 44px; }
</style>
</head>
<body>
  <main class="carton">
    <section class="lid">
      <svg class="lid-graphics" viewBox="0 0 560 560" width="560" height="560">
        <polygon points="0,300 210,165 430,165 560,70 560,115 440,200 230,200 0,345" fill="var(--race-red)"/>
        <polygon points="0,345 230,200 440,200 560,115 560,330 0,470" fill="var(--signal-yellow)"/>
        <polygon points="440,560 560,490 560,560" fill="var(--signal-yellow)"/>
        <polygon points="0,0 40,0 0,30" fill="var(--gold)"/>
      </svg>
      <div class="rider-artwork" role="img" aria-label="Faint line illustration of a motocross rider on a dirt bike"></div>
      <div class="brand-lockup"><span class="brand-dot"></span>VARONEL</div>
      <div class="lid-kicker">MOTOCYCLE</div>
      <div class="lid-title">BRAKEPADS</div>
    </section>

    <section class="front-panel">
      <svg viewBox="0 0 560 150" width="560" height="150">
        <polygon points="400,150 470,0 560,0 560,150" fill="var(--gold)"/>
        <polygon points="470,0 500,0 470,40" fill="var(--signal-yellow)"/>
      </svg>
      <div class="front-kicker">MOTOCYCLE</div>
      <div class="front-title">BRAKEPADS</div>
      <div class="brand-lockup"><span class="brand-dot"></span>VARONEL</div>
    </section>
  </main>
</body>
</html>
```